Product sheet for managing talented people!

We need a new product sheet to describe our method of helping organisations to manage their talented people! We have selected a rowing team as the graphical theme (sample attached - please select or suggest a new picture if you want). We have also attached a powerpoint slide with our model (this is the service we offer).

FRONT PAGE

We are looking for an eye-catching front page that uses our 1. "Kestrel Skills Model"; 2. a picture of a rowing team of 8, and 3. our logo and 1800 KESTRL phone number (1800 537 875).

Step 1 - Assess key positions to determine your Talent Management Priorities.

Step 2 - Organisational psychology support helps individuals self-evaluate (see page 2 for details).

Step 3 - Facilitate agreement with manager and embed best-practice in organisational fairness.

Step 4 - Tailor career development and redeployment options based on shared understanding.

Step 5 - Evaluate ROI for individual performance and engagement.

BACK PAGE

The second page will have more detail of each of the talent categories also included in the powerpoint slide. Logo attached also. Please also view our website as the graphics should give you a sense of the look and feel of our brand - www.kestrelsm.com.au We have also added another flyer that we still use - please do not reverse the logo on this project - use in current form. CORPORATE LOGO / COLOUR GUIDE
C100 M50 Y0 K0
C100 M50 Y0 K0
C100 M50 Y0 K0
Gradient
C100 M60 Y0 K40
C100 M45 Y0 K0
C100 M20 Y0 K0
C70 M0 Y0 K0
PMS 2935 C
PMS 2935 C 75% Tint
PMS 2935 C
PMS Process Cyan C

The successful flyer will need to be print ready (as per attached example) and in pdf form so that we can print and/or send as a PDF.

Thanks.

Target Market(s)

Human Resource Managers in business and government.

Industry/Entity Type

Product

Requirements
Must have
• Eye-catching graphics with a rowing team theme. Colours consistent with our corporate colour codes.
Nice to have
• Please add small "trademark" symbol to the logo. This is small TM in a circle and usually placed at top right hand of logo. PLease add our website address www.kestrelsm.com
Should not have
• Please do not "reverse" the logo - use as is.

```html
<!DOCTYPE html>
<html lang="en">
<head>
<meta charset="utf-8">
<title>Kestrel Skills Model – Product Sheet</title>
<link rel="stylesheet" href="https://fonts.googleapis.com/css2?family=Source+Sans+3:wght@300;400;700&family=Cormorant+Garamond:wght@400&display=swap">
<style>
  :root {
    --white: #ffffff;
    --brand: #0a62a8;
    --brand-light: #2a8fd0;
    --step-1: #62c8f0;
    --step-2: #22b6ea;
    --step-3: #129cd9;
    --step-4: #0a7bc2;
    --step-5: #0a4d86;
    --photo-top: #c9d9e6;
    --photo-mid: #6f93b0;
    --photo-low: #2e4f6c;
  }
  html, body {
    margin: 0;
    padding: 0;
    overflow: hidden;
    background: var(--white);
  }
  .sheet {
    position: relative;
    width: 848px;
    height: 1200px;
    overflow: hidden;
    background: var(--white);
    font-family: "Source Sans 3", "Helvetica Neue", Arial, sans-serif;
  }
  .hero-photo {
    position: absolute;
    left: 23px;
    top: 21px;
    width: 804px;
    height: 331px;
    background: linear-gradient(160deg, var(--photo-top) 0%, var(--photo-mid) 45%, var(--photo-low) 100%);
  }
  .headline {
    position: absolute;
    left: 23px;
    top: 374px;
    width: 804px;
    margin: 0;
    text-align: center;
    font-size: 27.5px;
    font-weight: 300;
    color: var(--brand-light);
    letter-spacing: 0.2px;
    white-space: nowrap;
  }
  .headline strong { font-weight: 700; }
  .steps {
    position: absolute;
    left: 23px;
    top: 439px;
    width: 804px;
    margin: 0;
    padding: 0;
    list-style: none;
  }
  .step {
    position: relative;
    height: 89px;
    color: var(--white);
  }
  .step--1 { background: var(--step-1); }
  .step--2 { background: var(--step-2); }
  .step--3 { background: var(--step-3); }
  .step--4 { background: var(--step-4); }
  .step--5 { background: var(--step-5); }
  .step-label {
    position: absolute;
    left: 62px;
    top: 30px;
    font-size: 19px;
    font-weight: 300;
  }
  .step-number {
    position: absolute;
    left: 120px;
    top: 6px;
    font-family: "Cormorant Garamond", "Times New Roman", serif;
    font-size: 64px;
    line-height: 1;
  }
  .step-text {
    position: absolute;
    left: 184px;
    top: 20px;
    margin: 0;
    font-size: 18.5px;
    font-weight: 400;
    line-height: 1.3;
  }
  .base-curve {
    position: absolute;
    left: 23px;
    top: 884px;
    width: 804px;
    height: 202px;
    display: block;
  }
  .base-curve path { fill: var(--step-5); }
  .brand {
    position: absolute;
    left: 0;
    top: 950px;
    width: 848px;
    text-align: center;
    color: var(--brand);
    font-weight: 400;
  }
  .brand-dot {
    display: block;
    width: 58px;
    height: 58px;
    margin: 0 auto 8px;
    border-radius: 50%;
    background: var(--brand);
  }
  .brand-name {
    display: block;
    font-size: 46px;
    line-height: 1;
    letter-spacing: 2px;
  }
  .brand-tag {
    display: block;
    margin-top: 6px;
    font-size: 13px;
    letter-spacing: 2.5px;
  }
  .footer {
    position: absolute;
    left: 28px;
    right: 28px;
    top: 1148px;
    display: flex;
    justify-content: space-between;
    font-size: 21px;
    font-weight: 400;
    color: var(--brand-light);
  }
  .footer-web { letter-spacing: 3.5px; }
  .footer-phone { letter-spacing: 1px; }
</style>
</head>
<body>
<main class="sheet">
  <div class="hero-photo" role="img" aria-label="Photograph of a women's rowing crew pulling their oars in unison, toned in blue"></div>

  <h1 class="headline">IS <strong>YOUR TEAM</strong> HEADING IN <strong>THE RIGHT DIRECTION?</strong></h1>

  <ol class="steps">
    <li class="step step--1">
      <span class="step-label">step</span>
      <span class="step-number">1</span>
      <p class="step-text">Agree business critical roles and determine<br>Talent Management priorities</p>
    </li>
    <li class="step step--2">
      <span class="step-label">step</span>
      <span class="step-number">2</span>
      <p class="step-text">Evaluate effectiveness of current Talent Management<br>and succession planning processes</p>
    </li>
    <li class="step step--3">
      <span class="step-label">step</span>
      <span class="step-number">3</span>
      <p class="step-text">Refine talent assessment process with a focus on people<br>in critical roles</p>
    </li>
    <li class="step step--4">
      <span class="step-label">step</span>
      <span class="step-number">4</span>
      <p class="step-text">Kestrel SM's organisational support assist<br>individuals' self-assessment</p>
    </li>
    <li class="step step--5">
      <span class="step-label">step</span>
      <span class="step-number">5</span>
      <p class="step-text">Measure ROI and embed continued<br>performance improvement</p>
    </li>
  </ol>

  <svg class="base-curve" viewBox="0 0 804 202" preserveAspectRatio="none" aria-hidden="true">
    <path d="M0 0 H804 V113 Q402 -57 0 113 Z"/>
  </svg>

  <div class="brand">
    <span class="brand-dot" aria-hidden="true"></span>
    <span class="brand-name">KESTREL</span>
    <span class="brand-tag">SKILLS MODEL</span>
  </div>

  <footer class="footer">
    <span class="footer-web">www.kestrelsm.com.au</span>
    <span class="footer-phone">Call 1800 KESTRL</span>
  </footer>
</main>
</body>
</html>
```